iOS App Design Project for Pebble Notes

We are looking for a redesign of the UI for our app, Pebble Notes. The app is a to-do list type app with 4 screens, and we already have a UI for it but we would like a nicer looking one that has a better colour scheme and is more intuitive.

We would like something that is a real treat to look at, and that users really want to use. Essentially what we want is the nicest and most simple design possible, as the current UI we have is not very user friendly.

The app is already on the market and is free so if you have an iOS device you can download it and take a look at it, and we have also included screenshots of the app.
Updates

Project Deadline Extended
Reason: I am updating the design brief and will also guarantee the payment.

Target Market(s)

Mobile users looking for simplicity

Requirements
Must have
• - Very visually pleasing
- Simple layout with minimal clutter
- Icons and buttons that explain what they do
Should not have
• Any features that detract from the simplicity of the app are not wanted.

```html
<!DOCTYPE html>
<html lang="en">
<head>
<meta charset="utf-8">
<title>My Tasks</title>
<link rel="stylesheet" href="https://fonts.googleapis.com/css2?family=Arimo:wght@400;700&family=Open+Sans:wght@400&display=swap">
<style>
  :root {
    --page-bg: #e8eaed;
    --status-top: #f4f4f4;
    --status-bottom: #c9c9c9;
    --status-text: #111111;
    --network-blue: #1d6fd6;
    --battery-green: #35c12b;
    --nav-top: #b0bccd;
    --nav-bottom: #7085a3;
    --nav-edge: #5b6e89;
    --nav-text: #ffffff;
    --nav-button-top: #6f8ab2;
    --nav-button-bottom: #3f5f8f;
    --task-top: #7890b8;
    --task-bottom: #4a6a9c;
    --task-rim: #f6f7f9;
    --task-text: #f4f6fa;
    --focus-glow: #1f7cff;
  }
  * { margin: 0; padding: 0; box-sizing: border-box; }
  html, body { width: 800px; height: 1200px; overflow: hidden; }
  body { background: var(--page-bg); position: relative; font-family: "Arimo", Arial, sans-serif; }

  .status-bar {
    position: absolute; left: 0; top: 0; width: 800px; height: 52px;
    background: linear-gradient(var(--status-top), var(--status-bottom));
    border-bottom: 1px solid #8e8e8e;
    color: var(--status-text); font-weight: 700; font-size: 31px;
  }
  .status-bar .carrier { position: absolute; left: 10px; top: 8px; display: flex; align-items: center; gap: 8px; }
  .status-bar .network { color: var(--network-blue); margin-left: 14px; }
  .status-bar .clock { position: absolute; left: 0; width: 800px; top: 8px; text-align: center; }
  .status-bar .power { position: absolute; right: 10px; top: 8px; display: flex; align-items: center; gap: 8px; }

  .nav-bar {
    position: absolute; left: 0; top: 52px; width: 800px; height: 123px;
    background: linear-gradient(var(--nav-top), var(--nav-bottom));
    border-bottom: 2px solid var(--nav-edge);
    box-shadow: 0 4px 6px rgba(0,0,0,0.15);
  }
  .nav-title {
    position: absolute; left: 0; width: 800px; top: 28px; text-align: center;
    color: var(--nav-text); font-weight: 700; font-size: 46px;
    text-shadow: 0 -2px 1px rgba(0,0,0,0.35);
  }
  .nav-button { position: absolute; top: 20px; width: 124px; height: 74px; }
  .nav-button.back { left: 24px; }
  .nav-button.next { right: 24px; }
  .nav-button span {
    position: absolute; top: 0; height: 74px; line-height: 74px;
    color: var(--nav-text); font-weight: 700; font-size: 28px;
    text-shadow: 0 -1px 1px rgba(0,0,0,0.4);
  }
  .nav-button.back span { left: 36px; }
  .nav-button.next span { left: 22px; }

  .task-list { position: absolute; left: 110px; top: 362px; width: 584px; list-style: none; }
  .task-button {
    height: 108px; margin-bottom: 69px; border-radius: 54px;
    border: 4px solid var(--task-rim);
    background: linear-gradient(var(--task-top) 0%, #6a84b0 48%, var(--task-bottom) 52%, var(--task-bottom) 100%);
    box-shadow: 0 2px 4px rgba(0,0,0,0.25), inset 0 2px 2px rgba(255,255,255,0.3);
    color: var(--task-text); font-family: "Open Sans", "Segoe UI", sans-serif;
    font-size: 50px; text-align: center; line-height: 98px;
    text-shadow: 0 -1px 1px rgba(0,0,0,0.25);
  }
  .task-button.is-selected {
    box-shadow: 0 -3px 0 -1px var(--focus-glow), 0 3px 0 -1px var(--focus-glow), 0 0 8px rgba(31,124,255,0.5);
  }
</style>
</head>
<body>
  <header class="status-bar">
    <div class="carrier">
      <svg width="50" height="22" viewBox="0 0 50 22" aria-hidden="true">
        <rect x="0" y="13" width="7" height="9" fill="#1d6fd6"/>
        <rect x="9" y="10" width="7" height="12" fill="#1d6fd6"/>
        <rect x="18" y="6" width="7" height="16" fill="#1d6fd6"/>
        <rect x="27" y="19" width="7" height="3" fill="#555"/>
        <rect x="36" y="19" width="7" height="3" fill="#555"/>
      </svg>
      <span class="carrier-name">Corella</span>
      <span class="network">3G</span>
    </div>
    <div class="clock">12:53 PM</div>
    <div class="power">
      <svg width="28" height="28" viewBox="0 0 28 28" aria-hidden="true">
        <circle cx="14" cy="14" r="12" fill="#6a6a6a"/>
        <path d="M14 6 V14 H9" stroke="#eee" stroke-width="3" fill="none"/>
      </svg>
      <span class="battery-level">81 %</span>
      <svg width="46" height="26" viewBox="0 0 46 26" aria-hidden="true">
        <rect x="1" y="2" width="38" height="22" rx="2" fill="#fff" stroke="#222" stroke-width="2"/>
        <rect x="4" y="5" width="32" height="16" fill="var(--battery-green)"/>
        <rect x="40" y="8" width="4" height="10" fill="#222"/>
        <path d="M24 5 L15 14 H21 L17 21 L27 11 H21 Z" fill="#111"/>
      </svg>
    </div>
  </header>

  <nav class="nav-bar">
    <a class="nav-button back">
      <svg width="124" height="74" viewBox="0 0 124 74" aria-hidden="true">
        <defs>
          <linearGradient id="navButtonFill" x1="0" y1="0" x2="0" y2="1">
            <stop offset="0" stop-color="var(--nav-button-top)"/>
            <stop offset="0.5" stop-color="#55729f"/>
            <stop offset="1" stop-color="var(--nav-button-bottom)"/>
          </linearGradient>
        </defs>
        <path d="M26 2 H114 Q122 2 122 10 V64 Q122 72 114 72 H26 L2 37 Z" fill="url(#navButtonFill)" stroke="#3c5275" stroke-width="2" stroke-linejoin="round"/>
      </svg>
      <span>Back</span>
    </a>
    <h1 class="nav-title">My Tasks</h1>
    <a class="nav-button next">
      <svg width="124" height="74" viewBox="0 0 124 74" aria-hidden="true">
        <path d="M98 2 H10 Q2 2 2 10 V64 Q2 72 10 72 H98 L122 37 Z" fill="url(#navButtonFill)" stroke="#3c5275" stroke-width="2" stroke-linejoin="round"/>
      </svg>
      <span>Next</span>
    </a>
  </nav>

  <ul class="task-list">
    <li class="task-button is-selected">Shopping</li>
    <li class="task-button">Homework</li>
    <li class="task-button">Task</li>
    <li class="task-button">Task</li>
  </ul>
</body>
</html>
```